Global Summit on Thermal Peptides

We are arranging a meeting in Finland in August: THE 8th GLOBAL SUMMIT ON THERMAL PEPTIDES IN LIFE AND HEALING - CELLULAR COPING ROUTES AND CIRCUITS.

The program and speakers are included in the Word files. The basic poster arrangement could be a little bit like in the Conference:
http://events.vorelka.org/files/posters/1483956274_17-regulators-plants.pdf

Basically only the organizers and invited speakers will be listed.

We would like to have some summery maritime background of the kind provided in the stock footage. In addition, we would include some summer views from the City of Turku. We have added a few potential University Campus views in the footage folder.

Reason: There was one design that was attractive. We wanted to extend the time available to work along the approach of this design.

Target Market(s)

Scientists in the field of cell stress research

Industry/Entity Type

Management

Requirements
Must have
• There must be the logo of our home university:
• https://www.lunvik.fi/personal/media/3991/lvenglogobasic4c.jpg
• ...somewhere down on the poster, a little bit like VRKA in the example above.
• There must also be the logo of the organizing organization Tissue Strain Global Fellowship:
• http://www.tissuestrainfellows.org/?
• All text should be readable (no light text on light background and vice versa)

```html
<!DOCTYPE html>
<html lang="en">
<head>
<meta charset="utf-8">
<title>Global Summit on Thermal Peptides 2017</title>
<link href="https://fonts.googleapis.com/css2?family=Roboto:wght@400;700;900&family=Roboto+Condensed:wght@300;400;700&display=swap" rel="stylesheet">
<style>
:root{
  --page:#1d5a86;
  --sky:#6d7377;
  --sunset:#c9742a;
  --dusk:#3a1d12;
  --body-top:#5e2c1c;
  --body-mid:#7e3f20;
  --body-bottom:#a9853a;
  --footer:#3a1510;
  --yellow:#ffe500;
  --heading:#f7d21a;
  --white:#ffffff;
  --soft:#f1e6dc;
  --red:#c4122f;
}
*{margin:0;padding:0;box-sizing:border-box}
html,body{width:1200px;height:1200px;overflow:hidden}
body{background:var(--page);font-family:"Roboto Condensed",Arial,sans-serif;color:var(--white)}
.poster{position:absolute;left:185px;top:20px;width:830px;height:1160px;overflow:hidden;
  background:linear-gradient(180deg,var(--body-top) 0%,var(--body-top) 45%,var(--body-mid) 68%,var(--body-bottom) 100%)}
.city-photo{position:absolute;left:0;top:0;width:830px;height:600px;
  background:
    radial-gradient(ellipse 160px 90px at 320px 310px,rgba(255,190,80,.9),rgba(255,150,40,0) 100%),
    linear-gradient(180deg,var(--sky) 0%,#8a7a6a 22%,var(--sunset) 38%,#7a3a1a 52%,var(--dusk) 64%,#5a3222 80%,rgba(94,44,28,0) 100%)}
.title-block{position:absolute;right:74px;top:38px;text-align:right;font-family:"Roboto",Arial,sans-serif}
.title-line1{font-size:41px;font-weight:400;line-height:1;letter-spacing:.3px}
.title-line1 .ordinal-the{font-size:34px;margin-right:6px}
.title-line1 .ordinal-num{font-size:66px;vertical-align:-4px}
.title-line1 sup{font-size:20px;vertical-align:38px;margin-right:14px}
.title-line2{font-size:29px;font-weight:400;margin-top:6px}
.title-line2 b{font-weight:900;font-size:32px}
.theme{position:absolute;left:0;width:830px;top:340px;text-align:center;font-family:"Roboto",Arial,sans-serif;
  font-weight:900;color:var(--yellow);font-size:52px;line-height:52px;letter-spacing:.5px}
.date-banner{position:absolute;left:314px;top:450px;width:516px;height:90px;background:rgba(70,28,18,.78);
  clip-path:polygon(70px 0,100% 0,100% 100%,0 100%)}
.date-text{position:absolute;right:62px;top:456px;text-align:right;font-family:"Roboto",Arial,sans-serif}
.date-main{font-size:45px;font-weight:400;line-height:50px}
.date-venue{font-size:19px;font-family:"Roboto Condensed",Arial,sans-serif;font-weight:300;margin-top:2px}
.col{position:absolute;top:556px}
.col-organizers{left:34px;width:300px}
.col-keynotes{left:359px;width:240px}
.col-invited{left:607px;width:220px}
.section-heading{color:var(--heading);font-weight:700;font-size:20px;line-height:24px}
.organizer{margin-top:10px;font-size:17.5px;line-height:25.5px;font-weight:300}
.organizer .person{font-weight:400}
.org-group{margin-top:14px}
.session-note{font-size:17px;font-weight:400;margin:10px 0 8px}
.speaker-list{list-style:none}
.speaker-list li{font-size:14px;line-height:20.5px;font-weight:300}
.speaker-list li b{font-weight:700}
.speaker-list.invited li{line-height:24.8px}
.col-invited .speaker-list li{line-height:29.4px}
.footer{position:absolute;left:0;top:1023px;width:830px;height:137px;background:var(--footer);
  clip-path:polygon(0 0,142px 0,142px 13px,688px 13px,688px 0,100% 0,100% 100%,0 100%)}
.footer-text{position:absolute;left:0;width:830px;top:1048px;text-align:center;font-size:22px;line-height:28px;font-weight:400;letter-spacing:.3px;
  font-family:"Roboto",Arial,sans-serif}
.partner-mark{position:absolute;top:1032px;width:98px;height:98px;background:var(--white);
  display:flex;flex-direction:column;align-items:center;justify-content:center;gap:8px;text-align:center}
.partner-mark.university{left:34px}
.partner-mark.society{left:697px}
.partner-mark .mark-name{font-family:"Roboto",Arial,sans-serif;font-weight:700;font-size:12px;line-height:13px;color:var(--footer)}
.mark-square{width:34px;height:34px;background:var(--red)}
.mark-circle{width:44px;height:44px;border-radius:50%;background:#2d8a8a}
</style>
</head>
<body>
<main class="poster">
  <div class="city-photo" role="img" aria-label="Turku city skyline at sunset reflected in the river"></div>

  <header class="title-block">
    <div class="title-line1"><span class="ordinal-the">The</span><span class="ordinal-num">8</span><sup>th</sup>GLOBAL SUMMIT ON</div>
    <div class="title-line2">THERMAL PEPTIDES IN <b>LIFE &amp; HEALING</b></div>
  </header>

  <h1 class="theme">CELLULAR COPING<br>ROUTES AND CIRCUITS</h1>

  <div class="date-banner"></div>
  <div class="date-text">
    <div class="date-main">August 13-17 2017</div>
    <div class="date-venue">Harborline Marina Hotel Turku, Finland</div>
  </div>

  <section class="col col-organizers">
    <h2 class="section-heading">ORGANIZER</h2>
    <p class="organizer"><span class="person">Mira Halvonen</span><br>Lunvik Akademi University<br>Finland</p>
    <h2 class="section-heading" style="margin-top:10px">CO-ORGANIZERS</h2>
    <p class="organizer"><span class="person">Erik Lundqvist</span><br>Lunvik Akademi University and<br>University of Saltvik Finland</p>
    <p class="organizer org-group"><span class="person">Gordon Ashfield</span><br>Tissue Strain Global Fellowship (TSGF)<br>University of Eastbrook USA</p>
    <p class="organizer org-group"><span class="person">Hélène Marchal</span><br>Université Rive Gauche<br>France</p>
  </section>

  <section class="col col-keynotes">
    <h2 class="section-heading">TSGF Congress 2017</h2>
    <p class="session-note">Keynotes (35 min + 10 min)</p>
    <ul class="speaker-list">
      <li><b>Clara Benedetti</b> UK</li>
      <li><b>Kirsi Aaltonen</b> Denmark</li>
      <li><b>Dan Hayashida</b> USA</li>
      <li><b>Paul Winter</b> USA</li>
    </ul>
    <h2 class="section-heading" style="margin-top:8px">Invited Speakers</h2>
    <p class="session-note" style="margin-top:14px">(20 min + 10 min)</p>
    <ul class="speaker-list invited">
      <li><b>Lucia Ferreira</b> Brazil</li>
      <li><b>Nadine Hollister</b> USA</li>
      <li><b>Simon Caldfield</b> USA</li>
      <li><b>Giulia Moretti</b> Italy</li>
      <li><b>Avi Levran</b> Israel</li>
      <li><b>Marco Delfino</b> USA</li>
      <li><b>Petya Ivanova-Draganova</b> UK</li>
      <li><b>Bruce T. Fairlow</b> USA</li>
      <li><b>Elena Navarro</b> France</li>
      <li><b>Karen Whitcombe</b> USA</li>
    </ul>
  </section>

  <section class="col col-invited" style="top:563px">
    <ul class="speaker-list">
      <li><b>Joost Vermaalen</b> The Netherlands</li>
      <li><b>Aino-Maria Rautio</b> Finland</li>
      <li><b>Stefan K. Brandt</b> Germany</li>
      <li><b>Hélène Marchal</b> France</li>
      <li><b>Derek L. Paxton</b> USA</li>
      <li><b>Hiroshi Tanabe</b> Japan (pending)</li>
      <li><b>Kenji Ohara</b> Japan</li>
      <li><b>Ray Dunmore</b> USA</li>
      <li><b>S. AlKhatiby</b> USA</li>
      <li><b>Pekka T. Voutilainen</b> Finland</li>
      <li><b>Margaret Halloway</b> USA</li>
      <li><b>Francesca Bellini</b> Italy</li>
      <li><b>David Ostrander</b> USA</li>
      <li><b>Victor E. Lambert</b> USA</li>
      <li><b>Ruth Kessler</b> USA Finland</li>
    </ul>
  </section>

  <footer class="footer"></footer>
  <div class="partner-mark university">
    <span class="mark-square"></span>
    <span class="mark-name">Lunvik Akademi University</span>
  </div>
  <p class="footer-text">TISSUE STRAIN GLOBAL FELLOWSHIP (TSGF)<br>LUNVIK AKADEMI UNIVERSITY (LAU)</p>
  <div class="partner-mark society">
    <span class="mark-circle"></span>
    <span class="mark-name">TSGF</span>
  </div>
</main>
</body>
</html>
```